Clean invitation for a wedding

Design a wedding invitation.
Those examples in attachment. They are looking for this style, about the same construction. Back with the symbols etc.

Clean sleek design.

marriage name:
Kemp & Rosetta
02.06.23

You can copy the rest of the texts from the examples.

```html
<!DOCTYPE html>
<html lang="en">
<head>
<meta charset="utf-8">
<title>Kemp &amp; Rosetta — Wedding Invitation</title>
<link rel="stylesheet" href="https://fonts.googleapis.com/css2?family=Sacramento&family=Montserrat:wght@400;700&family=DM+Serif+Display&display=swap">
<style>
  :root {
    --backdrop: #efe8e1;
    --card: #ffffff;
    --ink: #2b2b2b;
    --ink-soft: #444444;
    --icon-fill: #e4e0dc;
    --shadow: rgba(60, 40, 20, 0.12);
  }
  * { box-sizing: border-box; margin: 0; padding: 0; }
  html, body { width: 935px; height: 1200px; overflow: hidden; }
  body {
    background: var(--backdrop);
    position: relative;
    font-family: "Montserrat", sans-serif;
    color: var(--ink);
  }
  .card {
    position: absolute;
    top: 310px;
    width: 420px;
    height: 580px;
    background: var(--card);
    box-shadow: 0 6px 24px var(--shadow);
  }
  .card--program { left: 30px; }
  .card--invite { left: 485px; text-align: center; }

  /* Invitation */
  .invite__lead {
    margin-top: 92px;
    font-size: 12px;
    letter-spacing: 0.12em;
    line-height: 1.3;
    text-transform: uppercase;
    color: var(--ink-soft);
  }
  .invite__names {
    margin-top: 22px;
    font-family: "Sacramento", cursive;
    font-size: 96px;
    line-height: 0.78;
    color: var(--ink);
  }
  .invite__names .amp { display: block; font-size: 44px; line-height: 0.9; }
  .invite__date {
    margin-top: 56px;
    font-family: "DM Serif Display", serif;
    font-size: 42px;
    letter-spacing: 0.02em;
  }
  .invite__time {
    font-size: 11px;
    letter-spacing: 0.14em;
    text-transform: uppercase;
    color: var(--ink-soft);
  }
  .invite__venue {
    margin-top: 40px;
    font-size: 11px;
    letter-spacing: 0.12em;
    text-transform: uppercase;
    line-height: 1.4;
  }
  .invite__venue strong { display: block; font-weight: 700; }

  /* Program */
  .program__title {
    position: absolute;
    top: 40px;
    left: 0;
    width: 100%;
    text-align: center;
    font-family: "Sacramento", cursive;
    font-size: 64px;
    line-height: 1;
  }
  .program__timeline { position: absolute; left: 0; top: 0; }
  .program__item {
    position: absolute;
    left: 218px;
    font-size: 11px;
    letter-spacing: 0.06em;
    line-height: 1.2;
    color: var(--ink-soft);
  }
  .program__icon {
    position: absolute;
    left: 110px;
    width: 46px;
    height: 46px;
    border-radius: 10px;
    background: var(--icon-fill);
  }
</style>
</head>
<body>

  <section class="card card--program">
    <h2 class="program__title">Program</h2>

    <svg class="program__timeline" width="420" height="580" viewBox="0 0 420 580" aria-hidden="true">
      <line x1="200" y1="150" x2="200" y2="460" stroke="#2b2b2b" stroke-width="1.5"/>
      <circle cx="200" cy="150" r="5" fill="#2b2b2b"/>
      <circle cx="200" cy="212" r="5" fill="#2b2b2b"/>
      <circle cx="200" cy="274" r="5" fill="#2b2b2b"/>
      <circle cx="200" cy="336" r="5" fill="#2b2b2b"/>
      <circle cx="200" cy="398" r="5" fill="#2b2b2b"/>
      <circle cx="200" cy="460" r="5" fill="#2b2b2b"/>
    </svg>

    <div class="program__icon" style="top:160px" role="img" aria-label="Line icon of two wedding rings"></div>
    <div class="program__icon" style="top:222px" role="img" aria-label="Line icon of two clinking champagne glasses"></div>
    <div class="program__icon" style="top:284px" role="img" aria-label="Line icon of a tiered wedding cake"></div>
    <div class="program__icon" style="top:346px" role="img" aria-label="Line icon of a plate with fork and knife"></div>
    <div class="program__icon" style="top:408px" role="img" aria-label="Line icon of a couple dancing"></div>
    <div class="program__icon" style="top:480px" role="img" aria-label="Line icon of music notes"></div>

    <p class="program__item" style="top:128px">13.30<br>Wedding<br>Ceremony</p>
    <p class="program__item" style="top:198px">15.00<br>Cheers</p>
    <p class="program__item" style="top:256px">16.00<br>Cut the<br>Wedding Cake</p>
    <p class="program__item" style="top:322px">17.30<br>Dinner</p>
    <p class="program__item" style="top:380px">23.00<br>Wedding<br>Dance</p>
    <p class="program__item" style="top:442px">24.00<br>Casual<br>Event</p>
  </section>

  <section class="card card--invite">
    <p class="invite__lead">Please join us to<br>celebrate the wedding of</p>
    <h1 class="invite__names">Kemp<span class="amp">&amp;</span>Rosetta</h1>
    <p class="invite__date">02.06.23</p>
    <p class="invite__time">10’ clock in the afternoon</p>
    <p class="invite__venue"><strong>At Willow Creek Estate</strong>Malibu, California</p>
  </section>

</body>
</html>
```